"contact us" Flyer for Marketing Drop-offs

We need a simple 3rd of a page (3 3/4" x 8 1/2") flyer made for quick customer interaction.

These should display our logo, tagline, and our contact information. The background should incorporate the attached picture/color scheme.

This flyer will be offering an incentive to be determined at a later date.

Industry/Entity Type

Legal

Font styles to use
Serif
Sans Serif

Colors
0255a3
33a6d7
876aae

Requirements
Must have
• proper color scheme, simple/modern layout, attached logo
Nice to have
• creativity with working, placement
Should not have
• extra/meaningless characters, shapes

```html
<!DOCTYPE html>
<html lang="en">
<head>
<meta charset="utf-8">
<title>Mesa File – Contact Flyer</title>
<link rel="stylesheet" href="https://fonts.googleapis.com/css2?family=Raleway:wght@400;500;600;700;800&display=swap">
<style>
  :root {
    --brand-navy: #1f3a8f;
    --brand-blue: #0255a3;
    --brand-sky: #33a6d7;
    --brand-violet: #876aae;
    --paper: #ffffff;
    --stage: #e4e4e4;
    --photo-top: #8189c0;
    --photo-mid: #6470ab;
    --photo-low: #3e4a86;
    --field-text: #8a8f99;
  }
  * { box-sizing: border-box; margin: 0; padding: 0; }
  html, body {
    width: 1200px;
    height: 2372px;
    overflow: hidden;
    background: var(--stage);
    font-family: "Raleway", sans-serif;
  }
  .flyer {
    position: absolute;
    left: 120px;
    top: 36px;
    width: 960px;
    height: 2300px;
    background: var(--paper);
    overflow: hidden;
    box-shadow: 0 6px 24px rgba(0,0,0,0.18);
  }
  .landscape {
    position: absolute;
    left: 0;
    top: 0;
    width: 960px;
    height: 1560px;
    background: linear-gradient(180deg, var(--photo-top) 0%, var(--photo-mid) 50%, var(--photo-low) 100%);
  }
  .masthead-panel {
    position: absolute;
    left: 356px;
    top: 0;
    width: 604px;
    height: 330px;
    background: var(--paper);
  }
  .masthead-name {
    position: absolute;
    right: 60px;
    top: 138px;
    font-size: 112px;
    font-weight: 800;
    color: var(--brand-navy);
    letter-spacing: -2px;
    line-height: 1;
  }
  .tagline {
    position: absolute;
    left: 61px;
    top: 566px;
    width: 860px;
    padding-left: 75px;
    color: var(--paper);
    font-size: 38px;
    font-weight: 500;
    line-height: 47px;
  }
  .tagline strong { font-weight: 800; }
  .tagline-marker {
    position: absolute;
    left: 0;
    top: 6px;
    width: 20px;
    height: 170px;
    background: var(--brand-sky);
  }
  .tagline-marker::after {
    content: "";
    position: absolute;
    left: 27px;
    top: 0;
    width: 11px;
    height: 170px;
    background: var(--brand-blue);
  }
  .search-bar {
    position: absolute;
    left: 86px;
    top: 865px;
    width: 784px;
    height: 61px;
    display: flex;
  }
  .search-field {
    flex: 1;
    background: var(--paper);
    color: var(--field-text);
    font-size: 25px;
    line-height: 61px;
    padding-left: 28px;
  }
  .search-button {
    width: 200px;
    background: var(--brand-sky);
    color: var(--paper);
    font-size: 27px;
    font-weight: 500;
    display: flex;
    align-items: center;
    justify-content: center;
    gap: 10px;
  }
  .footer-name {
    position: absolute;
    left: 67px;
    top: 1632px;
    font-size: 78px;
    font-weight: 800;
    color: var(--brand-navy);
    letter-spacing: -1px;
    line-height: 1;
  }
  .cta-pill {
    position: absolute;
    left: 300px;
    top: 1824px;
    width: 360px;
    height: 60px;
    border-radius: 30px;
    background: var(--brand-violet);
    color: var(--paper);
    font-size: 35px;
    font-weight: 800;
    text-align: center;
    line-height: 60px;
    box-shadow: 0 10px 10px -6px rgba(0,0,0,0.35);
  }
  .contact {
    position: absolute;
    left: 95px;
    width: 770px;
    color: var(--brand-navy);
    font-weight: 600;
    display: flex;
    align-items: center;
    justify-content: center;
    gap: 12px;
    line-height: 1;
    font-size: 74px;
  }
  .contact-email { top: 1950px; }
  .contact-phone { top: 2056px; }
  .contact-rule {
    position: absolute;
    left: 95px;
    top: 2041px;
    width: 770px;
    height: 4px;
    background: var(--brand-blue);
  }
  .web-band {
    position: absolute;
    left: 178px;
    top: 2213px;
    width: 600px;
    height: 87px;
    background: var(--brand-sky);
    color: var(--paper);
    font-size: 54px;
    font-weight: 500;
    text-align: center;
    line-height: 87px;
  }
  .web-band strong { font-weight: 700; }
</style>
</head>
<body>
  <main class="flyer">
    <div class="landscape" role="img" aria-label="Photograph of a rocky canyon cliff over a river valley at dusk, tinted blue"></div>
    <div class="masthead-panel"></div>

    <div class="masthead-name">Mesa File</div>

    <p class="tagline">
      <span class="tagline-marker"></span>
      <strong>MesaFile</strong> is the premier source for<br>County Clerk Records and Mineral<br>Appraisal Data covering Texas, Oklahoma,<br>New Mexico and Colorado.
    </p>

    <div class="search-bar">
      <div class="search-field">One Click. Every County</div>
      <div class="search-button">
        <svg width="26" height="26" viewBox="0 0 26 26" aria-hidden="true">
          <circle cx="15" cy="11" r="8" fill="none" stroke="#fff" stroke-width="2.5"/>
          <line x1="9" y1="17" x2="2" y2="24" stroke="#fff" stroke-width="3" stroke-linecap="round"/>
        </svg>
        Search
      </div>
    </div>

    <div class="footer-name">Mesa File</div>

    <div class="cta-pill">GET IN TOUCH</div>

    <div class="contact contact-email">
      <svg width="50" height="36" viewBox="0 0 50 36" aria-hidden="true">
        <rect x="0" y="0" width="50" height="36" fill="var(--brand-blue)"/>
        <path d="M2,2 L25,20 L48,2 M2,34 L19,16 M48,34 L31,16" fill="none" stroke="#fff" stroke-width="3"/>
      </svg>
      info@mesafile.com
    </div>
    <div class="contact-rule"></div>
    <div class="contact contact-phone">
      <svg width="56" height="44" viewBox="0 0 56 44" aria-hidden="true">
        <path d="M4,16 C4,6 52,6 52,16 L44,20 L40,13 C33,10 23,10 16,13 L12,20 Z" fill="var(--brand-sky)"/>
        <path d="M14,22 L20,16 H36 L42,22 V40 H14 Z" fill="var(--brand-sky)"/>
        <circle cx="28" cy="30" r="6" fill="#fff"/>
      </svg>
      (555) 014-2290
    </div>

    <div class="web-band">www.<strong>mesafile</strong>.com</div>
  </main>
</body>
</html>
```